"The Craft of Patron Care," fourth edition cover design

Later this year, my publisher, Harold Penmarsh & Daughters, will issue a fourth, substantially revised edition of "The Craft of Patron Care," following the 2016 publication of the third edition and the second and first versions that were issued earlier.

To distinguish this new edition from previous ones, I need a cover design that visually connects and is consistent with what has preceded it, while signaling this is a new and different, worthy of prospective readers/buyers’ attention.

Attached are three different verbal approaches to the new cover; these are NOT MEANT to serve as actual designs, but rather will give you a sense of how language is to be deployed:

The first emphasizes “ART” as the key visual word in the book title;
The second emphasizes “CLIENT SERVICE” as the key visual words in the book title; and,
The third emphasizes just the word "CLIENT" in the book title.

A top-of-the-page is a pre-head that applies to all three versions:
“6 TIMELESS PRINCIPLES FOR ADVERTISING & MARKETING PRO’s
IN AN AI WORLD"

There's a mid-page sub-head for all three versions:
“THE CLASSIC GUIDE,” followed by
“FOURTH EDITION BY GERALD ASHCOMBE

And there's a one-line, bottom-of-the-page designation:
“Foreword by Mae Dunford, Global Executive Creative Director, Starbolt"

The pallette for the previously published third edition was black with red as an accent color on a field of white; I've attached a sample for reference, so you can see how it was executed. For this new fourth edition, I'd like to change the accent color from red to either Wedgewood blue, or British racing green, or an alternative that is assertive and color saturated -- think of primary colors -- that contrast sufficiently with the base of black. As an alternative, you can consider a cover that used either Wedgewood blue, British racing green, or another possibility as a full-bleed field, with copy content either revered out or surprinted.

Lastly, while the new cover largely is meant to be typographically driven, if you can come up with a visual metaphor that illustrates and builds on the book's title, that would be very helpful. By way of reference, the third edition's book cover attempted to do this by introducing a visual element at the end of the book's title that's meant to represent an artist's paint splatter (although I admit it didn't work as well as it should).

Target Market(s)

Prospective purchasers of the book who might discover copies at a bookstore, but more likely will encounter it through online distributors such as Riverdex, Hartwell & Pike, and Tindall’s.

Industry/Entity Type

Advertising and marketing

Font styles to use
Serif
Sans Serif
Other font styles liked:
• A mix of serif and san-serif typefaces is okay. for the examples I shared, I relieid on "Arial Rounded Bold" but you need not be weeded to this. If you opt to mix in a serif font, I am partial to Cambria as a typeface.

Requirements
Must have
• To achieve the goal of being “connected with but distinct” from previous editions, the new cover should be:  Largely typographic, but displaying a color palette different from the previous editions’ black-plus-red-accent on a canvas of white.  Any new accent color selected for use should be vibrant, strong, and highly saturated; think “British racing green,” “Wedgewood blue,” or their equivalents.  In addition to a powerful, “billboard” approach to type and color, consider other visual metaphors that are likely to engage the readers. The winning cover design will stand out from other books, while connecting with the previously published third edition.
Nice to have
• If you can find way to illustrate the book's title through a visual metaphor, that would be ideal.a
Should not have
• Anything that is frivolous or non-sensical

```html
<!DOCTYPE html>
<html lang="en">
<head>
<meta charset="utf-8">
<title>The Craft of Patron Care — Fourth Edition Cover</title>
<link rel="stylesheet" href="https://fonts.googleapis.com/css2?family=Jockey+One&family=Noto+Serif:ital@0;1&family=Black+Ops+One&family=Caveat:wght@500&display=swap">
<style>
  :root {
    --field: #0c3d0a;
    --sky: #7aaaf5;
    --sky-text: #79a9ef;
    --signal-red: #c8303c;
    --star-bronze: #5b4424;
    --star-teal: #2f6f5d;
  }
  * { margin: 0; padding: 0; box-sizing: border-box; }
  html, body { width: 800px; height: 1200px; overflow: hidden; background: var(--field); }
  .cover { position: relative; width: 800px; height: 1200px; background: var(--field); overflow: hidden; }

  .pre-head {
    position: absolute; left: 0; top: 74px; width: 800px; text-align: center;
    font-family: "Jockey One", "Arial Narrow", sans-serif; font-size: 29px; line-height: 1;
    color: var(--sky-text); letter-spacing: -0.3px; white-space: nowrap;
  }

  .rating-stars { position: absolute; left: 436px; top: 174px; width: 364px; height: 70px; }

  .edition-block { position: absolute; right: 20px; top: 300px; text-align: right; font-family: "Noto Serif", Cambria, serif; }
  .edition-block .guide { font-size: 31px; color: var(--sky-text); letter-spacing: 0.5px; line-height: 38px; }
  .edition-block .edition { font-size: 24px; color: var(--signal-red); letter-spacing: 1px; line-height: 30px; }

  .title-band { position: absolute; background: var(--sky); }
  .title-band--top { left: 232px; top: 389px; width: 568px; height: 128px; }
  .title-band--bottom { left: 164px; top: 534px; width: 636px; height: 147px; }

  .title-word {
    position: absolute; font-family: "Black Ops One", "Arial Black", sans-serif;
    color: var(--field); line-height: 1; white-space: nowrap;
  }
  .title-word--craft { left: 256px; top: 398px; font-size: 122px; }
  .title-word--care { left: 184px; top: 569px; font-size: 68px; letter-spacing: 2px; }

  .title-connector {
    position: absolute; font-family: "Caveat", cursive; font-weight: 500;
    color: var(--sky-text); line-height: 1; transform-origin: left top; transform: rotate(-90deg);
    white-space: nowrap;
  }
  .title-connector--the { left: 160px; top: 517px; font-size: 66px; letter-spacing: 4px; }
  .title-connector--of { left: 112px; top: 646px; font-size: 64px; }

  .credits { position: absolute; right: 20px; top: 700px; text-align: right; font-family: "Noto Serif", Cambria, serif; font-style: italic; }
  .credits .author { font-size: 34px; color: var(--signal-red); line-height: 44px; letter-spacing: 0.5px; }
  .credits .foreword { font-size: 17px; color: var(--sky-text); line-height: 22px; }

  .rule { position: absolute; left: 0; width: 800px; height: 3px; }
  .rule--sky { background: var(--sky); }
  .rule--red { background: var(--signal-red); }
</style>
</head>
<body>
<main class="cover">
  <p class="pre-head">6 TIMELESS PRINCIPLES FOR ADVERTISING &amp; MARKETING PROS IN AN&nbsp; A.I. WORLD</p>

  <svg class="rating-stars" viewBox="0 0 364 70" aria-hidden="true">
    <defs>
      <polygon id="star" points="0,-36 8.5,-11.5 34.2,-11.1 13.7,4.4 21.2,29.1 0,14.3 -21.2,29.1 -13.7,4.4 -34.2,-11.1 -8.5,-11.5"/>
    </defs>
    <use href="#star" x="36" y="38" fill="var(--star-bronze)"/>
    <use href="#star" x="109" y="38" fill="var(--star-teal)"/>
    <use href="#star" x="182" y="38" fill="var(--star-bronze)"/>
    <use href="#star" x="255" y="38" fill="var(--star-teal)"/>
    <use href="#star" x="328" y="38" fill="var(--star-bronze)"/>
  </svg>

  <div class="edition-block">
    <p class="guide">THE CLASSIC GUIDE</p>
    <p class="edition">FOURTH EDITION</p>
  </div>

  <h1 class="book-title">
    <span class="title-band title-band--top"></span>
    <span class="title-band title-band--bottom"></span>
    <span class="title-connector title-connector--the">THE</span>
    <span class="title-word title-word--craft">CRAFT</span>
    <span class="title-connector title-connector--of">OF</span>
    <span class="title-word title-word--care">PATRON CARE</span>
  </h1>

  <div class="credits">
    <p class="author">GERALD ASHCOMBE</p>
    <p class="foreword">Foreword by Mae Dunford, Global Executive<br>Creative Director, Starbolt</p>
  </div>

  <span class="rule rule--sky" style="top:1002px"></span>
  <span class="rule rule--red" style="top:1047px"></span>
  <span class="rule rule--red" style="top:1130px"></span>
  <span class="rule rule--sky" style="top:1172px"></span>
</main>
</body>
</html>
```